I need professional letterhead for an attorney. I already have my logo (attached). I currently have a project going to get business cards. I would like the letterhead to be classy. It is very important that this letterhead be in a format that I can import it into Microsoft Word 2013. I plan on importing this into Word so I can type my documents directly onto it and electronically send the finished documents to my clients. Thank you very much.

Industry/Entity Type

Attorney

Requirements
Must have
• Here is my info. Please put it all on there:
• Dwight R. Mallory Attorney At Law
• 48613 Brackwell Crescent
• St. Louis, MO 63047
• Telephone: 314-596-2043
• Fax: 800-627-4915
• Email: Dwight@RivermarkWills.com
• Also, I need the ability to import this final design into Microsoft Word 2013 so that I can type directly onto it. I believe I can do that if you hand it over to me as a JPG and a PDF in addition to the other formats. Then I should be able to import it into Word.

```html
<!DOCTYPE html>
<html lang="en">
<head>
<meta charset="utf-8">
<title>Rivermark Wills LLC — Letterhead</title>
<link rel="stylesheet" href="https://fonts.googleapis.com/css2?family=Cinzel:wght@500&family=Open+Sans:wght@400;700&display=swap">
<style>
  :root {
    --brand-blue: #1f6fbf;
    --ink: #2b2b2b;
    --corner-grey: #8d8d8d;
    --watermark: rgba(60, 60, 60, 0.07);
    --paper: #ffffff;
  }
  * { margin: 0; padding: 0; box-sizing: border-box; }
  html, body { width: 841px; height: 1200px; overflow: hidden; background: var(--paper); }
  .letterhead {
    position: relative;
    width: 841px;
    height: 1200px;
    background: var(--paper);
    font-family: "Open Sans", Arial, sans-serif;
    color: var(--ink);
    overflow: hidden;
  }
  .corner { position: absolute; display: block; }
  .corner--top { top: 0; left: 0; }
  .corner--bottom { right: 0; bottom: 0; }

  .brand {
    position: absolute;
    top: 52px;
    left: 118px;
    display: flex;
    align-items: center;
    gap: 14px;
  }
  .brand__mark {
    width: 30px;
    height: 30px;
    background: var(--brand-blue);
  }
  .brand__name {
    font-family: "Cinzel", "Times New Roman", serif;
    font-weight: 500;
    color: var(--brand-blue);
    font-size: 34px;
    line-height: 1;
    letter-spacing: 1px;
  }

  .attorney {
    position: absolute;
    top: 108px;
    right: 92px;
    text-align: right;
  }
  .attorney__name {
    font-size: 14px;
    font-weight: 700;
    color: var(--brand-blue);
    letter-spacing: 0.5px;
    text-transform: uppercase;
  }
  .attorney__title {
    font-size: 11px;
    color: var(--ink);
    margin-top: 2px;
  }

  .watermark {
    position: absolute;
    left: 50%;
    top: 690px;
    transform: translate(-50%, -50%) rotate(-34deg);
    font-family: "Cinzel", "Times New Roman", serif;
    font-weight: 500;
    color: var(--watermark);
    font-size: 92px;
    letter-spacing: 6px;
    white-space: nowrap;
    pointer-events: none;
    user-select: none;
  }

  .contact {
    position: absolute;
    left: 0;
    right: 0;
    bottom: 64px;
    text-align: center;
    font-size: 11px;
  }
  .contact__row {
    display: flex;
    justify-content: center;
    gap: 40px;
    margin-bottom: 10px;
  }
  .contact__item { display: inline-flex; align-items: center; gap: 7px; }
  .contact__dot {
    width: 9px;
    height: 9px;
    border-radius: 50%;
    background: var(--brand-blue);
  }
  .contact__address { font-size: 11px; }
</style>
</head>
<body>
  <main class="letterhead">
    <svg class="corner corner--top" width="100" height="125" viewBox="0 0 100 125" aria-hidden="true">
      <polygon points="0,0 100,0 0,125" fill="var(--brand-blue)"/>
    </svg>

    <header class="brand">
      <span class="brand__mark" aria-hidden="true"></span>
      <span class="brand__name">Rivermark Wills LLC</span>
    </header>

    <div class="attorney">
      <p class="attorney__name">Dwight R. Mallory</p>
      <p class="attorney__title">Attorney At Law</p>
    </div>

    <div class="watermark" aria-hidden="true">Rivermark Wills</div>

    <footer class="contact">
      <div class="contact__row">
        <span class="contact__item"><span class="contact__dot"></span>314-596-2043</span>
        <span class="contact__item"><span class="contact__dot"></span>800-627-4915</span>
        <span class="contact__item"><span class="contact__dot"></span>Dwight@RivermarkWills.com</span>
      </div>
      <p class="contact__address">48613 Brackwell Crescent St. Louis, MO 63047</p>
    </footer>

    <svg class="corner corner--bottom" width="110" height="140" viewBox="0 0 110 140" aria-hidden="true">
      <polygon points="110,0 110,140 0,140" fill="var(--corner-grey)"/>
    </svg>
  </main>
</body>
</html>
```